Industrial Professional Business Card Design (Vantrel KX)

Would like professional looking business cards. Not too busy leaning towards minimal. Should have a slogan like:
"Industrial Automation and Control".

We are a tech company that programs industrial PLC computers. We also develop custom hardware solutions. Please use the logo for inspiration.

Target Market(s)

Mining, industrial, processing, automation, factory

Industry/Entity Type

Engineering

Contact Information for Business Card

Name, phone, email, website. job title.

Font styles to use
Other font styles liked:
• droid sans

Requirements
Must have
• Use colours that go well with the logo. Not too busy design.

```html
<!DOCTYPE html>
<html lang="en">
<head>
<meta charset="utf-8">
<title>Vantrel KX — Business Card</title>
<link rel="stylesheet" href="https://fonts.googleapis.com/css2?family=Open+Sans:wght@400;600;700&display=swap">
<style>
  :root {
    --navy: #174a72;
    --orange: #f06a25;
    --white: #ffffff;
    --paper: #fbfbfb;
    --backdrop: #e8e6e7;
  }
  * { box-sizing: border-box; margin: 0; padding: 0; }
  html, body { width: 1200px; height: 1200px; overflow: hidden; background: var(--backdrop); }
  body { position: relative; font-family: "Open Sans", sans-serif; }

  .card {
    position: absolute;
    left: 275px;
    width: 649px;
    height: 405px;
    border-radius: 20px;
    overflow: hidden;
  }
  .card--front { top: 148px; background: var(--paper); }
  .card--back { top: 660px; background: var(--navy); }

  .front-shapes { position: absolute; inset: 0; width: 100%; height: 100%; }

  .name-tab {
    position: absolute; left: 0; top: 75px; width: 18px; height: 52px; background: var(--white);
  }
  .person-name {
    position: absolute; left: 40px; top: 66px;
    font-size: 31px; font-weight: 600; color: var(--orange); letter-spacing: 0.2px;
  }
  .person-title {
    position: absolute; left: 41px; top: 107px;
    font-size: 21px; color: var(--white);
  }

  .contact-list { position: absolute; left: 38px; top: 204px; list-style: none; }
  .contact-item {
    display: flex; align-items: center; height: 36px;
    font-size: 18.5px; color: var(--white); letter-spacing: 0.3px;
  }
  .contact-icon { width: 20px; height: 20px; margin-right: 12px; fill: var(--white); flex: none; }

  .brand-mark {
    position: absolute; border-radius: 50%;
  }
  .card--front .brand-mark { left: 487px; top: 78px; width: 70px; height: 70px; background: var(--navy); }
  .brand-name {
    position: absolute; left: 0; width: 100%; text-align: center;
    font-weight: 600; white-space: nowrap;
  }
  .card--front .brand-name { left: 372px; width: 300px; top: 156px; font-size: 35px; color: var(--navy); }

  .social-heading {
    position: absolute; left: 372px; width: 300px; top: 284px; text-align: center;
    font-size: 11px; font-weight: 600; color: var(--orange);
  }
  .social-links { position: absolute; left: 455px; top: 305px; display: flex; gap: 20px; }
  .social-dot { width: 30px; height: 30px; border: 1.6px solid var(--orange); border-radius: 50%; }

  .card--back .brand-mark { left: 292px; top: 128px; width: 92px; height: 92px; background: var(--white); }
  .card--back .brand-name { left: 174px; width: 300px; top: 226px; font-size: 36px; color: var(--white); }

  .back-rule {
    position: absolute; top: 381px; height: 0; border-top: 1px dashed rgba(255,255,255,0.8);
  }
  .back-rule--left { left: 0; width: 389px; }
  .back-rule--right { left: 618px; width: 31px; }
  .back-url {
    position: absolute; left: 408px; top: 367px;
    font-size: 18.5px; color: var(--white); letter-spacing: 0.3px;
  }
</style>
</head>
<body>

<section class="card card--front" aria-label="Business card front">
  <svg class="front-shapes" viewBox="0 0 649 405" preserveAspectRatio="none" aria-hidden="true">
    <path d="M338 0 L363 0 C425 110 428 280 292 405 L284 405 C400 285 398 110 338 0 Z" fill="var(--orange)"/>
    <path d="M0 0 L296 0 C372 110 376 290 287 405 L0 405 Z" fill="var(--navy)"/>
  </svg>

  <div class="name-tab"></div>
  <h1 class="person-name">Ronan Hale</h1>
  <p class="person-title">Founder &amp; CEO</p>

  <ul class="contact-list">
    <li class="contact-item">
      <svg class="contact-icon" viewBox="0 0 24 24" aria-hidden="true"><path d="M6.6 10.8a15.1 15.1 0 0 0 6.6 6.6l2.2-2.2a1 1 0 0 1 1-.25 11.4 11.4 0 0 0 3.6.57 1 1 0 0 1 1 1V20a1 1 0 0 1-1 1A17 17 0 0 1 3 4a1 1 0 0 1 1-1h3.5a1 1 0 0 1 1 1c0 1.25.2 2.45.57 3.57a1 1 0 0 1-.25 1z"/></svg>
      +100 555 010 20
    </li>
    <li class="contact-item">
      <svg class="contact-icon" viewBox="0 0 24 24" aria-hidden="true"><path d="M22 2 2 10.5l7 2.5 2 7 3.5-4.5L19 19z"/></svg>
      info@vantrelkx.example
    </li>
    <li class="contact-item">
      <svg class="contact-icon" viewBox="0 0 24 24" aria-hidden="true"><path d="M12 2a10 10 0 1 0 0 20 10 10 0 0 0 0-20zm6.9 6h-2.9a15.6 15.6 0 0 0-1.4-3.6A8 8 0 0 1 18.9 8zM12 4c.8 1.2 1.5 2.5 1.9 4h-3.8c.4-1.5 1.1-2.8 1.9-4zM4.3 14a8 8 0 0 1 0-4h3.4a16 16 0 0 0 0 4zm.8 2h2.9c.3 1.3.8 2.5 1.4 3.6A8 8 0 0 1 5.1 16zM8 8H5.1a8 8 0 0 1 4.3-3.6C8.8 5.5 8.3 6.7 8 8zm4 12c-.8-1.2-1.5-2.5-1.9-4h3.8c-.4 1.5-1.1 2.8-1.9 4zm2.3-6H9.7a14.7 14.7 0 0 1 0-4h4.6a14.7 14.7 0 0 1 0 4zm.3 5.6c.6-1.1 1.1-2.3 1.4-3.6h2.9a8 8 0 0 1-4.3 3.6zM16.3 14a16 16 0 0 0 0-4h3.4a8 8 0 0 1 0 4z"/></svg>
      www.vantrelkx.example
    </li>
    <li class="contact-item">
      <svg class="contact-icon" viewBox="0 0 24 24" aria-hidden="true"><path d="M12 2a7 7 0 0 0-7 7c0 5.2 7 13 7 13s7-7.8 7-13a7 7 0 0 0-7-7zm0 9.5A2.5 2.5 0 1 1 12 6.5a2.5 2.5 0 0 1 0 5z"/></svg>
      Street , Address , Country
    </li>
  </ul>

  <div class="brand-mark" aria-hidden="true"></div>
  <p class="brand-name">Vantrel KX</p>

  <p class="social-heading">FIND US ON SOCIAL MEDIA</p>
  <div class="social-links" aria-label="Social media links">
    <span class="social-dot"></span>
    <span class="social-dot"></span>
    <span class="social-dot"></span>
  </div>
</section>

<section class="card card--back" aria-label="Business card back">
  <div class="brand-mark" aria-hidden="true"></div>
  <p class="brand-name">Vantrel KX</p>
  <div class="back-rule back-rule--left"></div>
  <p class="back-url">www.vantrelkx.example</p>
  <div class="back-rule back-rule--right"></div>
</section>

</body>
</html>
```